**Business Card**Designs Project** LornaTrade,LLC

Im looking for a simple and elegant Business Card that has a professional Corporate look and feel. Im considering a Metal business card as well as 2 color layout, Embossed, 1 color two tone layout(File#6 like).

The card should NOT be too busy but subtle. Clean look providing Key Details.

please see uploaded files for actual logo and inspirational design i like.

See Uploaded File # 3 for Professional Logos Style

Target Market(s)

investors

Industry/Entity Type

Business

Contact Information for Business Card

Side 1 information
Lorna Trade,LLC - Description Text below main logo = (Funding - Sales) or (Commercial - Residential) or (Property - Funding )
www.lornatrade-demo.com

Side 2 Information =
Dov Pelkin | Managing Broker
P 555-014-7781 | F 555-016-2490
E info@lornatrade-demo.com
membership logos - see file #3 for stye and file #4 for inspiration

Side 2 = 10pt Font
BRE: 07281944
NMLS: 6620573

Colors
3277b5
5c5c5c
333333
959595
85acd3
1b1b1b
ffffff

Requirements
Must have
• Lorna Trade, LLC **G Logo** - See Uploaded File #5 ,
• Contact Information - See Business Card Details Above
• Web address = www.lornatrade-demo.com
• Membership logos - See Uploaded File #4 & 9
Nice to have
• 1 Color two tones, grey, White, Charcoal Grey, Dark Turquois, Dark blue, Slate blue,
• GOOD COMBINATIONS: White and Grey, white and Charcoal grey with a splash of blue, Charcoal grey card with White, etc..
• PLEASE TRY DARK BLUE DESIGNS
• Embossed, card designs
• Metal Business card design
Should not have
• I DONT LIKE ALOTE OF WAVE DESIGNS

```html
<!DOCTYPE html>
<html lang="en">
<head>
<meta charset="utf-8">
<title>Lorna Trade, LLC — Business Card</title>
<link href="https://fonts.googleapis.com/css2?family=Jost:wght@400;500&family=Michroma&family=Oswald:wght@600&family=Arimo:wght@400&display=swap" rel="stylesheet">
<style>
  :root {
    --stage: #141414;
    --charcoal: #1b1b1b;
    --charcoal-edge: #2a2a2a;
    --text-grey: #959595;
    --mid-grey: #5c5c5c;
    --dark-grey: #333333;
    --white: #ffffff;
    --teal: #4a9fb3;
    --blue: #3277b5;
    --metal-light: #d9d9d9;
    --metal-mid: #a9a9a9;
    --metal-dark: #8a8a8a;
    --emboss-light: #ececec;
    --emboss-shade: #6e6e6e;
  }
  * { box-sizing: border-box; margin: 0; padding: 0; }
  html, body { width: 1200px; height: 871px; overflow: hidden; }
  body {
    background: var(--stage);
    display: flex;
    align-items: center;
    justify-content: center;
    gap: 40px;
    font-family: "Jost", sans-serif;
  }

  .card {
    width: 540px;
    height: 308px;
    border-radius: 16px;
    position: relative;
    overflow: hidden;
  }

  /* ---------- Side 2: contact side ---------- */
  .card--contact {
    background: linear-gradient(160deg, var(--charcoal-edge), var(--charcoal) 60%);
  }
  .brand {
    position: absolute;
    display: flex;
    align-items: center;
  }
  .card--contact .brand { left: 26px; top: 124px; gap: 12px; }
  .brand__circle {
    border-radius: 50%;
    flex: none;
  }
  .card--contact .brand__circle {
    width: 50px; height: 50px;
    border: 4px solid var(--teal);
  }
  .brand__divider { align-self: stretch; width: 1px; }
  .card--contact .brand__divider { background: var(--text-grey); }
  .brand__text { display: flex; flex-direction: column; }
  .brand__name {
    font-weight: 500;
    letter-spacing: 0.04em;
    text-transform: uppercase;
    white-space: nowrap;
  }
  .card--contact .brand__name { font-size: 16px; color: var(--text-grey); line-height: 1.2; }
  .brand__rule { height: 1px; }
  .card--contact .brand__rule { background: var(--text-grey); margin: 3px 0 3px; }
  .brand__tagline {
    text-transform: uppercase;
    white-space: nowrap;
  }
  .card--contact .brand__tagline { font-size: 8px; letter-spacing: 0.1em; color: var(--text-grey); }

  .card__split {
    position: absolute;
    left: 290px; top: 70px;
    width: 2px; height: 170px;
    background: var(--teal);
  }
  .contact {
    position: absolute;
    left: 304px; top: 66px;
    color: var(--text-grey);
  }
  .contact__name {
    font-family: "Michroma", sans-serif;
    font-size: 18px;
    letter-spacing: 0.08em;
    color: var(--teal);
    text-transform: uppercase;
    line-height: 1.1;
  }
  .contact__title {
    font-family: "Michroma", sans-serif;
    font-size: 9px;
    letter-spacing: 0.14em;
    text-transform: uppercase;
    margin-bottom: 8px;
  }
  .contact__list { list-style: none; font-family: "Arimo", sans-serif; font-size: 15px; }
  .contact__list li { display: flex; align-items: center; gap: 10px; height: 23px; white-space: nowrap; }
  .contact__list svg { width: 15px; height: 13px; fill: var(--text-grey); flex: none; }
  .licenses {
    position: absolute;
    right: 30px; bottom: 30px;
    font-family: "Oswald", sans-serif;
    font-weight: 600;
    font-size: 14px;
    color: var(--mid-grey);
    letter-spacing: 0.02em;
  }

  /* ---------- Side 1: metal logo side ---------- */
  .card--metal {
    background: linear-gradient(135deg, #f4f4f4, var(--metal-light) 40%, #eaeaea);
    padding: 12px;
  }
  .metal-plate {
    width: 100%; height: 100%;
    border-radius: 12px;
    background: linear-gradient(160deg, var(--metal-mid), #bdbdbd 45%, var(--metal-dark));
    position: relative;
  }
  .card--metal .brand { left: 30px; top: 56px; gap: 16px; }
  .card--metal .brand__circle {
    width: 92px; height: 92px;
    border: 8px solid var(--emboss-light);
    box-shadow: 1px 1px 0 var(--emboss-shade), inset 1px 1px 0 var(--emboss-shade);
  }
  .card--metal .brand__divider { background: var(--emboss-light); box-shadow: 1px 0 0 var(--emboss-shade); }
  .card--metal .brand__name {
    font-size: 28px;
    color: var(--emboss-light);
    text-shadow: 1px 1px 0 var(--emboss-shade);
  }
  .card--metal .brand__rule { background: var(--emboss-light); margin: 5px 0 3px; box-shadow: 0 1px 0 var(--emboss-shade); }
  .card--metal .brand__tagline {
    font-size: 14px; letter-spacing: 0.14em;
    color: var(--emboss-light);
    text-shadow: 1px 1px 0 var(--emboss-shade);
  }
  .web {
    position: absolute;
    left: 0; right: 0; bottom: 62px;
    text-align: center;
    font-size: 22px;
    letter-spacing: 0.06em;
    color: var(--emboss-light);
    text-shadow: 1px 1px 0 var(--emboss-shade);
  }
</style>
</head>
<body>

  <section class="card card--contact" aria-label="Business card, contact side">
    <div class="brand">
      <span class="brand__circle"></span>
      <span class="brand__divider"></span>
      <div class="brand__text">
        <span class="brand__name">Lorna Trade LLC</span>
        <span class="brand__rule"></span>
        <span class="brand__tagline">Commercial &amp; Residential</span>
      </div>
    </div>

    <span class="card__split"></span>

    <div class="contact">
      <p class="contact__name">Dov Pelkin</p>
      <p class="contact__title">Managing Broker</p>
      <ul class="contact__list">
        <li>
          <svg viewBox="0 0 16 14" aria-label="Phone"><path d="M1 4c0-2 2-3 7-3s7 1 7 3v1h-4V4H5v1H1zM3 6h10l2 7H1z"/></svg>
          555.013.2208
        </li>
        <li>
          <svg viewBox="0 0 16 14" aria-label="Fax"><path d="M4 0h8v4H4zM1 5h14v9H1zM3 8h6v1H3zm0 2h6v1H3z"/></svg>
          555-016-2490
        </li>
        <li>
          <svg viewBox="0 0 16 14" aria-label="Email"><path d="M1 2h14v10H1zM2 3l6 5 6-5v1L8 9 2 4z"/></svg>
          info@lornatrade-demo.com
        </li>
      </ul>
    </div>

    <p class="licenses">BRE: 07281944 NMLS: 6620573</p>
  </section>

  <section class="card card--metal" aria-label="Business card, metal logo side">
    <div class="metal-plate">
      <div class="brand">
        <span class="brand__circle"></span>
        <span class="brand__divider"></span>
        <div class="brand__text">
          <span class="brand__name">Lorna Trade LLC</span>
          <span class="brand__rule"></span>
          <span class="brand__tagline">Commercial &amp; Residential</span>
        </div>
      </div>
      <p class="web">www.lornatrade-demo.com</p>
    </div>
  </section>

</body>
</html>
```